Home page web design for a lawn specialist business

-The design must be based around the attached HPID (home page information design) called Turf Tidings HPID. I've attached Word and PDF versions - these are the same. The table boxes are just for approximate placement of information and you can use boxes and bold shapes for this design.

All fonts used in the HPID are only examples - you can use any Google font you wish.

- Text that is in orange is for your information only. Text to go on the design is black. Some instructions are in the HPID. Please be creative!

-The design needs to be modern and exciting - colours are to be the green of the logo, and white ...and then choose dark green, or dark grey or black.

Logo - attached (it's not great quality but don't worry, we'll replace it later)

- I've provided the images for the galleries - they are labelled and will match the name in the HPID. Please use the supplied images!

- Examples of some websites that have great design... don't copy them please but they are similar in look to what we are after....
www.qmbbuildworks.co.nz
http://www.rim-safeguard.co.nz/
http://www.lumenhomes.wb.gs/

Important: Width of content will be 1280 pixels when implemented as a web page but the winning design will need to supplied be on a 2000 pixel wide background so nav bars and background can extend outside the 1280 width.
Header height (without nav bar) 150-160 pixels.

We don't comment on individual designs but will choose a winning design promptly.

Industry/Entity Type

Business

Number of Pages Required

1 page

Font styles to use
Sans Serif

Requirements
Must have
• clean, modern, well-spaced design

```html
<!DOCTYPE html>
<html lang="en">
<head>
<meta charset="utf-8">
<title>Turf Tidings – Lawn specialists</title>
<link href="https://fonts.googleapis.com/css2?family=Raleway:wght@400;500;600;700&family=Open+Sans:wght@400;600&display=swap" rel="stylesheet">
<style>
:root{
  --green:#3fae2a;
  --green-light:#5fcc3a;
  --green-dark:#2f8f1f;
  --band-top:#8ee05e;
  --band-bottom:#3cb52a;
  --ink:#222;
  --text:#555;
  --muted:#888;
  --grey-band:#e4e4e4;
  --pale:#f7f7f7;
  --footer:#2b2b2b;
  --footer-base:#222;
  --field:#444;
  --orange:#f39c12;
  --white:#fff;
}
*{box-sizing:border-box;margin:0;padding:0}
html,body{width:1200px;height:2535px;overflow:hidden}
body{position:relative;background:var(--white);font-family:'Open Sans',sans-serif;color:var(--text)}
.abs{position:absolute}
h1,h2,h3,h4,.raleway{font-family:'Raleway',sans-serif;font-weight:400}

/* header */
.brand{left:186px;top:42px;display:flex;align-items:center;gap:12px}
.brand-square{width:40px;height:40px;background:var(--green)}
.brand-name{font-family:'Raleway',sans-serif;font-weight:700;font-size:30px;color:var(--green)}
.header-info{right:152px;top:24px;text-align:right;font-family:'Raleway',sans-serif}
.header-info .title{font-size:20px;color:#444}
.header-info .line{font-size:12.5px;color:#aaa;line-height:22px}
.header-info .phone{font-size:23px;color:#222;font-weight:500;display:flex;align-items:center;justify-content:flex-end;gap:6px;margin-top:4px}

/* nav */
.nav{left:0;top:135px;width:1200px;height:46px;background:linear-gradient(var(--green-light),var(--green))}
.nav ul{list-style:none;display:flex;position:absolute;left:150px;top:0;height:46px}
.nav li{font-size:14px;color:var(--white);padding:0 14px;line-height:46px;border-right:1px solid rgba(0,0,0,.15);font-family:'Open Sans',sans-serif}
.nav li:last-child{border-right:none}

/* hero */
.hero-band{left:0;top:181px;width:1200px;height:279px;background:var(--grey-band)}
.slider{left:152px;top:198px;width:892px;height:441px;background:var(--white);padding:8px;box-shadow:0 2px 8px rgba(0,0,0,.25)}
.slider-photo{width:100%;height:100%;background:linear-gradient(90deg,#7d6a5a 0%,#8a7868 45%,#6fb53c 55%,#4f9a2a 100%)}
.tag{font-family:'Raleway',sans-serif;font-weight:700;color:var(--white);font-size:30px;background:rgba(40,40,40,.85);clip-path:polygon(8% 0,100% 0,92% 100%,0 100%);padding:4px 50px}
.tag-before{left:348px;top:462px}
.tag-after{left:572px;top:412px}
.arrow{top:370px}

/* intro */
.intro{left:0;top:680px;width:1200px;text-align:center}
.intro h1{font-size:30px;color:#222}
.intro h2{font-size:22px;color:#333;margin-top:4px}
.intro p{width:900px;margin:16px auto 0;font-size:11.5px;line-height:21px;color:#555}

/* cards */
.card{width:443px;height:281px;background:var(--white);border:1px solid #ddd;box-shadow:0 1px 3px rgba(0,0,0,.1)}
.card-photo{height:152px}
.card h3{font-size:17px;color:#333;margin:16px 18px 6px}
.card p{font-size:10.5px;line-height:18px;color:#888;margin:0 18px}
.card-btn{position:absolute;left:0;bottom:0;width:100%;height:34px;background:linear-gradient(var(--green-light),var(--green));color:var(--white);font-size:13px;font-weight:600;line-height:34px;padding-left:25px;letter-spacing:.3px}

/* video section */
.about-band{left:0;top:1563px;width:1200px;height:347px;background:var(--pale)}
.video-title{left:151px;top:1598px;font-size:17px;color:#333;line-height:23px}
.video-frame{left:154px;top:1656px;width:367px;height:198px;background:linear-gradient(#6b8a5a,#5d9a3a 60%,#4f8a2a)}
.play{left:312px;top:1730px}
.about-title{left:613px;top:1604px;font-size:32px;color:#222}
.about-text{left:613px;top:1656px;width:430px;font-size:11.5px;line-height:23px;color:#555}
.btn-dark{left:612px;top:1808px;width:126px;height:31px;background:#222;color:var(--white);font-size:12.5px;line-height:31px;text-align:center;border-radius:2px}

/* testimonial */
.quote-band{left:0;top:1910px;width:1200px;height:275px;background:linear-gradient(var(--band-top),var(--band-bottom))}
.quote{left:164px;top:1980px;width:470px;color:var(--white)}
.quote h4{font-size:22px;line-height:27px;font-weight:500}
.quote p{font-size:13px;line-height:20px;margin-top:14px;color:#eaffdf}
.quote .who{font-size:15px;color:#111;margin-top:16px}
.quote .role{font-size:11.5px;color:#111}
.quote-photo{left:715px;top:1972px;width:329px;height:152px;background:linear-gradient(#6a8a4a,#5cb83a 55%,#3f9a25)}

/* footer */
.footer{left:0;top:2185px;width:1200px;height:286px;background:var(--footer)}
.footer-links{left:166px;top:2224px;list-style:none}
.footer-links li{font-size:13px;color:#eee;line-height:23px}
.badge{left:409px;top:2224px;width:177px;height:206px;background:var(--white)}
.badge-shape{position:absolute;left:38px;top:36px;width:100px;height:130px;border-radius:50% 50% 8px 8px;background:linear-gradient(#b8dc4a,#5fa52f)}
.form-head{left:659px;top:2224px;font-family:'Raleway',sans-serif;color:var(--white);font-size:16px;line-height:24px}
.field{height:24px;background:var(--field);color:#bbb;font-size:10px;line-height:24px;padding-left:12px}
.cta{left:661px;top:2412px;width:128px;height:32px;background:var(--orange);color:var(--white);font-weight:600;font-size:12.5px;line-height:32px;text-align:center}
.base{left:0;top:2471px;width:1200px;height:64px;background:var(--footer-base)}
.copyright{left:172px;top:2496px;font-size:10.5px;color:#888}
.social{right:160px;top:2492px;display:flex;gap:14px}
.social span{width:20px;height:20px;border-radius:50%;background:#ddd}
</style>
</head>
<body>

<header>
  <div class="abs brand"><span class="brand-square"></span><span class="brand-name">Turf Tidings</span></div>
  <div class="abs header-info">
    <div class="title">Lawn specialists</div>
    <div class="line">from ground preparation to lawn aftercare</div>
    <div class="line">Servicing the Auckland region</div>
    <div class="phone">
      <svg width="20" height="20" viewBox="0 0 24 24"><path fill="#3fae2a" d="M6.6 10.8a15.1 15.1 0 0 0 6.6 6.6l2.2-2.2a1 1 0 0 1 1-.25 11.4 11.4 0 0 0 3.6.57 1 1 0 0 1 1 1V20a1 1 0 0 1-1 1A17 17 0 0 1 3 4a1 1 0 0 1 1-1h3.5a1 1 0 0 1 1 1c0 1.25.2 2.45.57 3.57a1 1 0 0 1-.25 1z"/></svg>
      0800 41 62 90
    </div>
  </div>
</header>

<nav class="abs nav">
  <ul>
    <li>Home</li><li>About us</li><li>Services</li><li>Lawn care</li><li>Seasonal care</li><li>Hydroseeding</li><li>FAQs</li><li>Before &amp; After</li><li>Gallery</li><li>Quote / Contact</li>
  </ul>
</nav>

<section>
  <div class="abs hero-band"></div>
  <div class="abs slider"><div class="slider-photo" role="img" aria-label="Garden beside a house shown as bare soil on one side and finished green lawn on the other"></div></div>
  <div class="abs tag tag-after">AFTER</div>
  <div class="abs tag tag-before">BEFORE</div>
  <svg class="abs arrow" style="left:176px" width="28" height="66" viewBox="0 0 28 66"><polyline points="24,2 4,33 24,64" fill="none" stroke="#fff" stroke-width="2"/></svg>
  <svg class="abs arrow" style="left:1000px" width="28" height="66" viewBox="0 0 28 66"><polyline points="4,2 24,33 4,64" fill="none" stroke="#fff" stroke-width="2"/></svg>
</section>

<section class="abs intro">
  <h1>You can always spot an Turf Tidings lawn</h1>
  <h2>It's the one that turns your neighbours green with envy.</h2>
  <p>you want a lawn or playing field that looks good throughout the year, talk to us. Turf Tidings are New Zealand's experts in high quality grass seeding and lawn maintenance, creating the lushest lawns you'll ever see. With high-tech equipment, years of experience and expert aftercare, nobody knows grass like Turf Tidings. There are many factors that influence the quality of a lawn, including seasonality, growing conditions, shade, seed types, and time. A one-size-fits-all solution couldn't possibly guarantee a great lawn, so we provide personalised advice, a full range of seeding techniques</p>
</section>

<section>
  <article class="abs card" style="left:149px;top:943px">
    <div class="card-photo" role="img" aria-label="Freshly hydroseeded front yard with garden plants" style="background:linear-gradient(#7a7a5a,#3f8a86 60%,#2f7a78)"></div>
    <h3>Grass seeding services</h3>
    <p>With a wide range of grass seed applications to choose from, including hydroseeding and instant lawn, there is an option to suit your property and your requirements.</p>
    <div class="card-btn">MORE ABOUT GRASS SEEDING</div>
  </article>
  <article class="abs card" style="left:608px;top:943px">
    <div class="card-photo" role="img" aria-label="Sprinkler watering a green lawn" style="background:linear-gradient(#a8c88a,#5aa838 55%,#3d8a22)"></div>
    <h3>Lawn care maintenance</h3>
    <p>As well as lawn care services, the team at Turf Tidings provides helpful information for regular upkeep of your residential or commercial lawn.</p>
    <div class="card-btn">MORE ABOUT ONGOING LAWN CARE</div>
  </article>
  <article class="abs card" style="left:149px;top:1237px">
    <div class="card-photo" role="img" aria-label="Raised lawn bed beside a large tree" style="background:linear-gradient(#7a8a6a,#6a9a4a 50%,#3f9a25)"></div>
    <h3>FAQs about grass seeding and lawn care</h3>
    <p>For more information, read our frequently asked questions regarding grass seeding and lawn care.</p>
    <div class="card-btn">GRASS SEEDING &amp; LAWN CARE FAQS</div>
  </article>
  <article class="abs card" style="left:608px;top:1237px">
    <div class="card-photo" role="img" aria-label="Backyard before and after seeding, side by side" style="background:linear-gradient(90deg,#4a7a78 0%,#3f7a76 48%,#6ab83f 52%,#4f9a2a 100%)"></div>
    <h3>Before and after lawn photos</h3>
    <p>See what you potential new lawn could look like by viewing a range of before and after lawn seeding photos.</p>
    <div class="card-btn">BEFORE AND AFTER PHOTOS</div>
  </article>
</section>

<section>
  <div class="abs about-band"></div>
  <h3 class="abs video-title">Watch the video on how Turf Tidings can transform<br>your empty spaces into beautiful green grass lawns</h3>
  <div class="abs video-frame" role="img" aria-label="Video still of a house with a new green lawn"></div>
  <svg class="abs play" width="50" height="50" viewBox="0 0 50 50"><circle cx="25" cy="25" r="25" fill="#fff"/><polygon points="20,15 20,35 36,25" fill="#222"/></svg>
  <h2 class="abs about-title">Turf Tidings</h2>
  <div class="abs about-text">
    <p>For all things grass, you need the best! Turf Tidings are skilled specialists when it comes to creating the perfect lawn for your property.</p>
    <p>From pre-seeding preparation to a full range of grass seeding services and lawn after care options, you'll enjoy a healthy green lawn for many years.</p>
    <p>Selling your property? Turf Tidings will add the wow factor to the outdoor areas of your home with a lush green lawn.</p>
  </div>
  <div class="abs btn-dark">Find Out More</div>
</section>

<section>
  <div class="abs quote-band"></div>
  <blockquote class="abs quote">
    <h4 class="raleway">I would recommend Turf Tidings to anyone who wants an amazing lawn</h4>
    <p>Donec dictum lectus non odio Cras a ante vitae enim iaculis aliquam Mauris nunc quam venenatis nec euismod sit amet egestas placerat est</p>
    <div class="who">Dan Hollis</div>
    <div class="role">Homeowner, Greenhithe</div>
  </blockquote>
  <div class="abs quote-photo" role="img" aria-label="Lawn mower cutting a green lawn"></div>
</section>

<footer>
  <div class="abs footer"></div>
  <ul class="abs footer-links">
    <li>Home</li><li>About us</li><li>Services</li><li>Lawn care</li><li>Seasonal care</li><li>Hydroseeding</li><li>FAQs</li><li>Before &amp; After Gallery</li><li>Quote / Contact</li>
  </ul>
  <div class="abs badge"><span class="badge-shape"></span></div>
  <div class="abs form-head">Get a quote for your new lawn!<br>Fill in the form or phone us on 0800 41 62 90.</div>
  <div class="abs field" style="left:661px;top:2282px;width:166px">First name</div>
  <div class="abs field" style="left:837px;top:2282px;width:166px">Last name</div>
  <div class="abs field" style="left:661px;top:2314px;width:166px">Email address</div>
  <div class="abs field" style="left:837px;top:2314px;width:166px">Contact Phone</div>
  <div class="abs field" style="left:661px;top:2347px;width:342px;height:55px;line-height:20px;padding-top:2px">Details</div>
  <div class="abs cta">CALL ME BACK</div>
  <div class="abs base"></div>
  <div class="abs copyright">© 2015 Company Name &nbsp;All right reserved &nbsp;Term of Use</div>
  <div class="abs social"><span></span><span></span><span></span></div>
</footer>

</body>
</html>
```